Fundraising Company Needs a Brochure Design

We need a brochure design for a company that helps charities raise money. Our main product is selling art on easels to raise money for various charites. The brochure will have a total of four pages with the size being 8.5" X 11" for each page. All of text will be provided for the brochure. The front page should include our logo and a short intro. The second page will contain a summary along with how the easel program works. The third page will contain information about the companies and charities we work with and other ways we raise money for charities. The back page will contain three testimonials along with our mission/vision statement and our contact information. We also need to include a picture of the easel somewhere in the catalog. The color of our logo is orange and light green but the brochure doesn't need to contain those colors.
The brochure will be presented to major charities and local businesses alike.
It Company

```html
<!DOCTYPE html>
<html lang="en">
<head>
<meta charset="utf-8">
<title>Bids for Good – Summary and How It Works</title>
<link href="https://fonts.googleapis.com/css2?family=Source+Sans+3:wght@300;400&display=swap" rel="stylesheet">
<style>
  :root {
    --orange: #f26b23;
    --green: #8dc63f;
    --panel: #edf3df;
    --heading: #2f5f33;
    --body: #4a4a45;
    --paper: #ffffff;
    --backdrop: #ffffff;
  }
  * { box-sizing: border-box; margin: 0; padding: 0; }
  html, body { width: 1200px; height: 1200px; overflow: hidden; background: var(--backdrop); }
  body { font-family: "Source Sans 3", "Myriad Pro", sans-serif; color: var(--body); position: relative; }
  .page { position: absolute; left: 165px; top: 45px; width: 857px; height: 1110px; overflow: hidden; background: var(--paper); }
  .page-bg { position: absolute; inset: 0; }
  .panel { position: absolute; background: var(--panel); border-radius: 18px; }
  .panel-summary { left: 30px; top: 232px; width: 430px; height: 645px; }
  .panel-how { left: 428px; top: 88px; width: 397px; height: 932px; }
  .content { position: absolute; }
  .kicker { font-size: 16px; font-weight: 400; color: var(--heading); line-height: 20px; }
  .title { font-size: 30px; font-weight: 300; color: var(--heading); line-height: 37px; margin-top: 4px; }
  .text { font-size: 13px; line-height: 16.8px; font-weight: 400; color: var(--body); }
  .text p { margin-bottom: 16.8px; }
  .bullets { list-style: none; margin-bottom: 24px; }
  .bullets li { padding-left: 7px; text-indent: -7px; margin-bottom: 8px; }
  .bullets li::before { content: "• "; }
  .summary-block { left: 50px; top: 250px; width: 360px; }
  .summary-block .text { margin-top: 17px; }
  .how-block { left: 448px; top: 106px; width: 358px; }
  .how-block .text { margin-top: 16px; }
  .easel-title { font-size: 29px; font-weight: 300; color: var(--heading); line-height: 36px; margin: 14px 0 10px; }
  .easel-text { width: 275px; }
  .easel-photo { position: absolute; left: 728px; top: 820px; width: 72px; height: 180px;
    background: linear-gradient(180deg, #8a6a2c 0%, #5a4a2a 45%, #b33a2a 60%, #e8e4de 80%, #3a2a22 100%); border-radius: 2px; }
</style>
</head>
<body>
  <div class="page">
    <svg class="page-bg" width="857" height="1110" viewBox="0 0 857 1110" aria-hidden="true">
      <rect width="857" height="1110" fill="var(--orange)"/>
      <path d="M0,95 C150,160 300,205 440,232 L440,700 C300,600 120,480 0,430 Z" fill="var(--paper)"/>
      <ellipse cx="650" cy="12" rx="105" ry="95" fill="var(--paper)"/>
      <path d="M857,830 C800,950 740,1050 705,1110 L857,1110 Z" fill="var(--paper)"/>
      <path d="M857,340 C835,420 830,510 857,605 Z" fill="var(--green)"/>
    </svg>

    <div class="panel panel-summary"></div>
    <div class="panel panel-how"></div>

    <section class="content summary-block">
      <h2 class="kicker">Bids for Good –</h2>
      <h1 class="title">Summary</h1>
      <div class="text">
        <p>Bids for Good was created as a new way for communities to work together and collectively raise money for deserving charities. We help charitable organizations, local establishments, and citizens to work hand in hand, to help those in need. At Bids for Good, we bring charity, business, and people together to help raise money through Sealed Bid Auctions.</p>
        <ul class="bullets">
          <li>Establishments host a rotating collection of art, appropriately selected for their type of organization or business.</li>
          <li>Generous customers submit bids, on location, for the art, with the highest bidder claiming the piece of art.</li>
          <li>The establishment gets increased traffic and helps a charity of their choice.</li>
          <li>The charity selected by the establishment receives a portion of the profits from the auction.</li>
        </ul>
        <p>A Sealed Bid Auction, organized by Bids for Good, is an ideal way for businesses and other establishments to fundraise for a charity of their choice. There are no costs for the hosts associated with the auction and all auction materials are supplied by Bids for Good. We handle all the details, manage the auction, handle the presentation and delivery of the art, and oversee the completion of the purchases. The only cost to the host establishment is four square feet of floor space.</p>
        <p>Bids for Good has raised thousands of dollars for many different charities, both large and small, for special projects or long-term initiatives. The simplicity of this program is what makes it successful, but bringing a community together to help those in need makes everyone a winner.</p>
      </div>
    </section>

    <section class="content how-block">
      <h2 class="kicker">Bids for Good –</h2>
      <h1 class="title">Sealed Bid Auctions and How They Work</h1>
      <div class="text">
        <p>Sealed Bid Auctions, organized by Bids for Good, are effortless but rewarding ways for local establishments and organizations to raise money for charities of their choice.</p>
        <p>It’s easier than you think. In a host’s space, a piece of art is put up for auction. Customers interested in owning the art submit bid amounts on pieces of paper on location by sealing their bid in an envelope and placing it in a box. There will be a minimum bid for each item in an auction. This will be the original cost for the item up for bid plus additional costs incurred in the process of readying it for auction. The highest bid wins the auction and the item is sold. Profit from the auction goes to a charity preselected by the location hosting the auction.</p>
        <p>The auctions are an easy and straightforward process for both the hosts and the charities. Bids for Good takes care of all the details. We supply the artwork and a smart easel on which to display it. We provide the signage and Sealed Bid Auction materials, contact the winner, and manage the purchase and delivery details. Any other associated effort or costs are also our responsibility.</p>
        <p>The four square feet of floor space, donated by the host establishment, will host a new piece of art every three weeks. Each piece of art is selected with the charity or the host establishment in mind. They are typically limited edition oil paintings or prints including works by the Northern Painters Circle, selected photography, as well as sport and music inspired art. An employee from Bids for Good handles the replacement of each piece of art, and readies the space for the next three weeks of sealed bidding.</p>
        <p>The original cost of the artwork, and other associated costs generate the minimum bid, while every cent surpassing the minimum goes directly to the chosen charity.</p>
      </div>
      <h2 class="easel-title">Easel Text to go here</h2>
      <p class="text easel-text">EaselOssunt. Omnim quossin net dolor aut est officil laceate molorum eum rerumquas digenectus earia alitis a parum animus. Etur modis inctemp oremolu pturerio. Nequame quat qui ide nonectat volessin necaepe et faccusae ma ducim resto eos estiis eosam conseditas nonsectate nonsequi verehendae</p>
    </section>

    <div class="easel-photo" role="img" aria-label="Photo of a framed painting displayed on a wooden easel with a sealed bid sign below"></div>
  </div>
</body>
</html>
```